Bright Ledger Path's Mortgage Arc

For BrightLedgerPath.org - Creating a sequence of web pages for consumers to understand their mortgage through Mortgage Arc. There are six pages - want the designer to be willing to design and code those six pages. Most of the pages are very similar.

```html
<!DOCTYPE html>
<html lang="en">
<head>
<meta charset="utf-8">
<title>Bright Ledger Path – Mortgage Arc</title>
<link href="https://fonts.googleapis.com/css2?family=Poppins:wght@300;400;500;600;700&display=swap" rel="stylesheet">
<style>
:root{
  --canvas:#ffffff;
  --top-bar:#1a80d6;
  --nav-blue:#0a2bc6;
  --primary:#0f2ecf;
  --login-green:#1fc77c;
  --footer-blue:#1b6fd2;
  --section-grey:#f1f1f1;
  --card:#ffffff;
  --field-yellow:#ffff00;
  --ink:#2a2a2a;
  --muted:#4a4a4a;
  --line:#9a9a9a;
}
*{box-sizing:border-box;margin:0;padding:0}
html,body{width:1200px;height:2691px;overflow:hidden;background:var(--canvas);font-family:"Poppins",sans-serif;color:var(--ink)}
.page{position:absolute;left:141px;width:908px;background:#fff;box-shadow:0 8px 28px rgba(0,0,0,.22)}
.page--home{top:122px}
.page--profile{top:988px}

.top-bar{height:41px;background:var(--top-bar);position:relative}
.login-btn{position:absolute;left:374px;top:6px;width:64px;height:29px;background:var(--login-green);border:1px solid #e9fff4;color:#fff;font-size:12px;font-weight:500;display:flex;align-items:center;justify-content:center}

.main-nav{height:73px;background:var(--nav-blue);display:flex;align-items:center;padding:0 83px 0 81px;justify-content:space-between}
.brand{display:flex;align-items:center;gap:9px;color:#fff;font-size:16px;font-weight:500}
.brand-mark{width:22px;height:22px;background:#fff;border-radius:3px}
.nav-links{display:flex;gap:21px;color:#fff;font-size:12px;font-weight:500}

.hero{position:relative;height:416px;overflow:hidden}
.hero-photo{position:absolute;inset:0;background:linear-gradient(100deg,#6b5a4a 0%,#9b8266 25%,#c9b39a 45%,#e7dfd6 62%,#d3c2ae 78%,#7a5a44 100%)}
.hero-panel{position:absolute;left:82px;top:108px;width:356px;height:196px;background:rgba(120,120,120,.55)}
.hero-rule{position:absolute;left:80px;top:73px;width:3px;height:260px;background:var(--primary)}
.hero-copy{position:absolute;left:97px;top:122px;color:#fff}
.hero-kicker{font-size:19px;font-weight:300}
.hero-title{margin-top:10px;font-size:22px;font-weight:700;line-height:26px}
.hero-title .accent{color:var(--primary)}
.hero-stat{margin-top:9px;font-size:19px;font-weight:300}
.btn-start{margin-top:14px;width:108px;height:32px;border-radius:16px;background:var(--primary);color:#fff;font-size:11px;font-weight:600;display:flex;align-items:center;justify-content:space-between;padding:0 8px 0 15px}

.arrow-icon{width:20px;height:20px}

.menu{position:relative;height:211px;background:#fff}
.page--profile .menu{height:218px}
.menu-grid{position:absolute;left:84px;top:64px;display:grid;grid-template-columns:repeat(4,168px);column-gap:22px;row-gap:16px}
.menu-pill{height:36px;border:1px solid #9aa0aa;border-radius:18px;font-size:10px;display:flex;align-items:center;justify-content:center;color:#333;background:#fff}
.menu-pill--active{background:var(--primary);border-color:var(--primary);color:#fff;font-weight:600}

.site-footer{height:43px;background:var(--footer-blue);position:relative;color:#fff;font-size:8px}
.copyright{position:absolute;left:83px;top:12px}
.social{position:absolute;left:418px;top:12px;display:flex;gap:4px}
.social span{width:22px;height:22px;border-radius:50%;background:#e7eefb}
.legal{position:absolute;left:682px;top:12px}
.page-code{position:absolute;left:873px;top:15px;font-size:8px}

.profile{position:relative;height:758px;background:var(--section-grey)}
.profile-title{position:absolute;left:0;width:908px;top:52px;text-align:center;font-size:25px;font-weight:700;color:#222}
.card{position:absolute;background:var(--card);border-radius:4px;box-shadow:0 2px 8px rgba(0,0,0,.18)}
.card-caption{font-size:11px;font-weight:500;color:#333;text-align:center;margin-top:10px}
.pill-value{margin:6px auto 0;width:120px;height:23px;border-radius:12px;background:var(--primary);color:#fff;font-size:8px;font-weight:600;display:flex;align-items:center;justify-content:center}
.purpose{left:363px;top:100px;width:181px;height:68px}
.payment{left:380px;top:184px;width:149px;height:72px}
.down{left:380px;top:265px;width:149px;height:68px}

.action-outline,.action-solid{position:absolute;left:637px;width:230px;height:32px;border-radius:16px;font-size:11px;display:flex;align-items:center;justify-content:space-between;padding:0 10px 0 15px}
.action-outline{top:67px;border:1px solid #8a8f99;background:#fff;color:#333}
.action-solid{top:112px;background:var(--primary);color:#fff;font-weight:600}

.info{top:184px;width:288px;height:252px;padding:22px 9px 0 9px}
.info--personal{left:80px}
.info--mortgage{left:543px}
.info-row{display:grid;grid-template-columns:150px 120px;align-items:center;height:36px;font-size:10px;color:var(--muted)}
.info-row .heading{font-size:12px;font-weight:700;color:#222}
.field{height:24px;border:1px solid var(--line);border-radius:2px;background:#fff;font-size:8px;font-weight:600;display:flex;align-items:center;justify-content:center;color:#222}
.field--yellow{background:var(--field-yellow);border-color:#c9c400}
.field--blue{background:var(--primary);border-color:var(--primary);color:#fff}
.field-pair{display:grid;grid-template-columns:56px 56px;gap:8px}

.property{left:80px;top:459px;width:751px;height:252px}
.property-title{position:absolute;left:0;width:751px;top:20px;text-align:center;font-size:12px;font-weight:700}
.property-divider{position:absolute;left:374px;top:56px;width:1px;height:170px;background:#cfcfcf}
.prop-col{position:absolute;top:56px}
.prop-col--left{left:53px}
.prop-col--right{left:411px}
.prop-row{display:grid;align-items:center;height:36px;font-size:10px;color:var(--muted)}
.prop-col--left .prop-row{grid-template-columns:150px 121px}
.prop-col--right .prop-row{grid-template-columns:160px 121px}
.prop-row .field-pair{grid-template-columns:56px 56px;gap:9px}
.stack-labels{line-height:16px;padding-left:8px}
.terms{display:grid;grid-template-columns:82px 38px 121px;column-gap:0;font-size:10px;color:var(--muted);height:72px}
.terms .stack-labels{padding-left:17px;padding-top:2px}
.terms .short{width:36px;margin-top:4px}
.terms .boxes{display:flex;flex-direction:column;gap:12px;grid-column:3;padding-top:4px}
</style>
</head>
<body>

<!-- Home page -->
<div class="page page--home">
  <div class="top-bar"><div class="login-btn">LOG IN</div></div>
  <nav class="main-nav">
    <div class="brand"><span class="brand-mark"></span>Bright Ledger Path</div>
    <div class="nav-links"><span>Home</span><span>Testimonials</span><span>Programs</span><span>FAQ ▾</span><span>Blog</span><span>Podcast</span></div>
  </nav>
  <section class="hero">
    <div class="hero-photo" role="img" aria-label="Photo of a smiling woman in a café holding a phone and a bank card"></div>
    <div class="hero-panel"></div>
    <div class="hero-rule"></div>
    <div class="hero-copy">
      <div class="hero-kicker">Recognized as</div>
      <div class="hero-title">THE BEST <span class="accent">Credit Score</span><br><span class="accent">Improvement</span> PROGRAM</div>
      <div class="hero-stat">81 Average Point Improvement</div>
      <div class="btn-start">Get Started
        <svg class="arrow-icon" viewBox="0 0 20 20"><path d="M3 17 L8 11 L11 13 L16 5" stroke="#fff" stroke-width="2.2" fill="none"/><path d="M12 4 H17 V9" stroke="#fff" stroke-width="2.2" fill="none"/></svg>
      </div>
    </div>
  </section>
  <section class="menu">
    <div class="menu-grid">
      <div class="menu-pill menu-pill--active">Edit Mortage Profile</div>
      <div class="menu-pill">Maximum Mortgage Qualification</div>
      <div class="menu-pill">Specific Mortgage Amount</div>
      <div class="menu-pill">Specific Mortgage Payment</div>
      <div class="menu-pill">Conventional Mortgage Options</div>
      <div class="menu-pill">FHA Mortgage Options</div>
      <div class="menu-pill">VA Mortgage Options</div>
      <div class="menu-pill">USDA Mortgage Options</div>
    </div>
  </section>
  <footer class="site-footer">
    <div class="copyright">Copyright 2023 by Bright Ledger Path</div>
    <div class="social"><span></span><span></span><span></span></div>
    <div class="legal">Terms Of Use &nbsp;|&nbsp; Privacy Statement</div>
    <div class="page-code">C44</div>
  </footer>
</div>

<!-- Mortgage profile page -->
<div class="page page--profile">
  <div class="top-bar"><div class="login-btn">LOG IN</div></div>
  <nav class="main-nav">
    <div class="brand"><span class="brand-mark"></span>Bright Ledger Path</div>
    <div class="nav-links"><span>Home</span><span>Testimonials</span><span>Programs</span><span>FAQ ▾</span><span>Blog</span><span>Podcast</span></div>
  </nav>
  <section class="hero">
    <div class="hero-photo" role="img" aria-label="Photo of a smiling woman in a café holding a phone and a bank card"></div>
    <div class="hero-panel"></div>
    <div class="hero-rule"></div>
    <div class="hero-copy">
      <div class="hero-kicker">Recognized as</div>
      <div class="hero-title">THE BEST <span class="accent">Credit Score</span><br><span class="accent">Improvement</span> PROGRAM</div>
      <div class="hero-stat">81 Average Point Improvement</div>
      <div class="btn-start">Get Started
        <svg class="arrow-icon" viewBox="0 0 20 20"><path d="M3 17 L8 11 L11 13 L16 5" stroke="#fff" stroke-width="2.2" fill="none"/><path d="M12 4 H17 V9" stroke="#fff" stroke-width="2.2" fill="none"/></svg>
      </div>
    </div>
  </section>
  <section class="menu">
    <div class="menu-grid">
      <div class="menu-pill menu-pill--active">Edit Mortage Profile</div>
      <div class="menu-pill">Maximum Mortgage Qualification</div>
      <div class="menu-pill">Specific Mortgage Amount</div>
      <div class="menu-pill">Specific Mortgage Payment</div>
      <div class="menu-pill">Conventional Mortgage Options</div>
      <div class="menu-pill">FHA Mortgage Options</div>
      <div class="menu-pill">VA Mortgage Options</div>
      <div class="menu-pill">USDA Mortgage Options</div>
    </div>
  </section>

  <section class="profile">
    <h2 class="profile-title">Your Mortgage Profile</h2>

    <div class="action-outline">Review Questions
      <svg class="arrow-icon" viewBox="0 0 20 20"><path d="M3 17 L8 11 L11 13 L16 5" stroke="var(--primary)" stroke-width="2.2" fill="none"/><path d="M12 4 H17 V9" stroke="var(--primary)" stroke-width="2.2" fill="none"/></svg>
    </div>
    <div class="action-solid">Save &amp; Return to Mortgage Central
      <svg class="arrow-icon" viewBox="0 0 20 20"><path d="M3 17 L8 11 L11 13 L16 5" stroke="#fff" stroke-width="2.2" fill="none"/><path d="M12 4 H17 V9" stroke="#fff" stroke-width="2.2" fill="none"/></svg>
    </div>

    <div class="card purpose"><div class="card-caption">Purpose of Mortgage</div><div class="pill-value">Purchase</div></div>
    <div class="card payment"><div class="card-caption">Payment Amount</div><div class="pill-value">$2,000</div></div>
    <div class="card down"><div class="card-caption">Down Payment</div><div class="pill-value">Least Amount</div></div>

    <div class="card info info--personal">
      <div class="info-row"><span class="heading">Personal information</span><div class="field field--blue">Purchase</div></div>
      <div class="info-row"><span>Monthly Gross Income:</span><div class="field">10,000</div></div>
      <div class="info-row"><span>Pay Off Any Debt?</span><div class="field-pair"><div class="field field--yellow">No</div><div class="field field--yellow">400</div></div></div>
      <div class="info-row"><span>Previous Homeowner (3Yrs?)</span><div class="field field--yellow">No</div></div>
      <div class="info-row"><span>Numer In Household:</span><div class="field field--yellow">4</div></div>
      <div class="info-row"><span>Coborrower / Spouse on Loan</span><div class="field field--yellow">No</div></div>
    </div>

    <div class="card info info--mortgage">
      <div class="info-row"><span class="heading">Mortgage Information</span><span></span></div>
      <div class="info-row"><span>Loan Purpose:</span><div class="field field--yellow">Purchase</div></div>
      <div class="info-row"><span>Term</span><div class="field field--yellow">30 Year</div></div>
      <div class="info-row"><span>Type of Interest Rate</span><div class="field field--yellow">Fixed</div></div>
      <div class="info-row"><span>Annual Property Taxes:</span><div class="field">$2,000</div></div>
      <div class="info-row"><span>Annual Home Insurance</span><div class="field">$600</div></div>
    </div>

    <div class="card property">
      <div class="property-title">Property Information</div>
      <div class="property-divider"></div>
      <div class="prop-col prop-col--left">
        <div class="prop-row"><span>Own Other Property / Rents:</span><div class="field-pair"><div class="field field--yellow">No</div><div class="field">$0</div></div></div>
        <div class="prop-row"><span>Occupancy:</span><div class="field field--yellow">Live in It</div></div>
        <div class="prop-row"><span>Type of Home:</span><div class="field field--yellow">SFR</div></div>
        <div class="prop-row"><span>Property Location:</span><div class="field field--yellow">Utah</div></div>
        <div class="prop-row"><span class="stack-labels">State:<br>County:</span><div class="field field--yellow">Salt Lake</div></div>
      </div>
      <div class="prop-col prop-col--right">
        <div class="prop-row"><span>Number of Units:</span><div class="field field--yellow">1</div></div>
        <div class="prop-row"><span>Total Monthly Rents - 2-4 Units</span><div class="field field--yellow">N/A</div></div>
        <div class="prop-row"><span>2nd Mortgage:</span><div class="field field--yellow"></div></div>
        <div class="terms">
          <span class="stack-labels">Term:<br>Balance:<br>Interest rate:</span>
          <div class="field field--yellow short">N</div>
          <div class="boxes"><div class="field"></div><div class="field"></div></div>
        </div>
      </div>
    </div>
  </section>

  <footer class="site-footer">
    <div class="copyright">Copyright 2023 by Bright Ledger Path</div>
    <div class="social"><span></span><span></span><span></span></div>
    <div class="legal">Terms Of Use &nbsp;|&nbsp; Privacy Statement</div>
    <div class="page-code">C44</div>
  </footer>
</div>

</body>
</html>
```